Velintu Yoga Centre

• Only boutique Yoga Centre which practices Yoga in traditional way.

• Only six members in one session to provide personal attention to each member.

• Many different styles of Yoga, Meditation and Vinyasana.

• Yoga and Ayurvedic Centre provides holistic approach in many ways with Ayurvedic doctors and qualified therapists with an array of all naturopathic and Ayurvedic medicine.

• Only Ayurvedic Centre with Therapeutic massage tables with made with Medicinal wood and genuine herbal oils from India and Sri Lanka

Industry/Entity Type

Boutique

```html
<!DOCTYPE html>
<html lang="en">
<head>
<meta charset="utf-8">
<title>Velintu Ayurvedic &amp; Yoga Centre – Flyer</title>
<link rel="stylesheet" href="https://fonts.googleapis.com/css2?family=Source+Sans+3:ital,wght@0,300;0,400;0,600;0,700;1,400&display=swap">
<style>
  :root {
    --page-bg: #eef3c6;
    --cell-green: #eef2c9;
    --cell-rose: #ecddd2;
    --line: #c9cfa6;
    --brown: #9b6b3e;
    --brown-dark: #6b4a2c;
    --ink: #2b2b2b;
    --green: #2f8a3f;
    --white: #ffffff;
    --shadow: rgba(0,0,0,0.35);
  }
  * { box-sizing: border-box; margin: 0; padding: 0; }
  html, body { width: 1200px; height: 900px; overflow: hidden; background: var(--white); }
  body { position: relative; font-family: "Source Sans 3", sans-serif; color: var(--ink); }

  .page {
    position: absolute;
    background: var(--page-bg);
    box-shadow: 3px 3px 5px var(--shadow);
    border: 1px solid #999;
    overflow: hidden;
  }
  .page--back { left: 8px; top: 42px; width: 565px; height: 803px; }
  .page--front { left: 616px; top: 42px; width: 560px; height: 801px; }

  .top-strip {
    position: absolute; left: 0; top: 0; width: 100%; height: 36px;
    background: var(--white);
  }
  .top-strip__title {
    position: absolute; right: 10px; top: 8px;
    font-style: italic; font-size: 17px; color: var(--brown);
  }
  .foot-strip {
    position: absolute; left: 0; bottom: 0; width: 100%; height: 32px;
    background: var(--white);
    text-align: center; font-size: 14px; line-height: 32px; color: var(--brown);
  }

  .brand-tab {
    position: absolute; background: var(--white);
    display: flex; flex-direction: column; align-items: center; justify-content: flex-end;
    text-align: center;
  }
  .page--back .brand-tab { left: 20px; top: 36px; width: 148px; height: 188px; border-radius: 0 0 74px 74px; padding-bottom: 42px; }
  .page--front .brand-tab { left: 163px; top: 0; width: 227px; height: 318px; border-radius: 0 0 113px 113px; padding-bottom: 70px; }
  .brand-tab__dot { border-radius: 50%; background: #a8cf4a; margin-bottom: 14px; }
  .page--back .brand-tab__dot { width: 58px; height: 58px; }
  .page--front .brand-tab__dot { width: 110px; height: 110px; margin-bottom: 22px; }
  .brand-tab__name { color: var(--green); font-weight: 600; line-height: 1.05; }
  .page--back .brand-tab__name { font-size: 19px; }
  .page--front .brand-tab__name { font-size: 31px; }

  .intro {
    position: absolute; left: 206px; top: 56px; width: 330px;
    font-size: 10.5px; line-height: 17.3px; color: var(--ink);
  }

  .schedule-title {
    position: absolute; left: 70px; top: 266px;
    font-size: 21px; font-weight: 400; color: var(--brown-dark); letter-spacing: 0.3px;
  }
  .schedule-sub {
    position: absolute; left: 74px; top: 293px;
    font-size: 13px; color: var(--brown);
  }
  .schedule-sub strong { font-weight: 700; color: var(--brown); }

  .timetable {
    position: absolute; left: 19px; top: 328px; width: 497px;
    border-collapse: collapse; border: 1px solid #555;
    font-size: 10px; table-layout: fixed;
  }
  .timetable th, .timetable td {
    height: 19.5px; padding: 0 5px; text-align: left;
    border-bottom: 1px solid var(--line);
    background: var(--cell-green);
  }
  .timetable th { font-weight: 700; font-size: 10.5px; height: 21px; }
  .timetable .rose { background: var(--cell-rose); }

  .photo { position: absolute; }
  .photo--sea { background: linear-gradient(180deg, #3b4552 0%, #6e6a66 55%, #c9714a 100%); }
  .photo--stretch { background: linear-gradient(135deg, #c7d84a 0%, #a8bb3a 55%, #d65a6a 100%); }
  .photo--sea-day { background: linear-gradient(180deg, #8dbbe6 0%, #3d6fae 45%, #5d9a43 70%, #d98a4a 100%); }
  .photo--stretch-day { background: linear-gradient(135deg, #d9dcc8 0%, #c9b9a6 50%, #c23a63 100%); }

  .contact {
    position: absolute; left: 378px; top: 622px;
    font-size: 12px; color: var(--brown); line-height: 17px;
  }
  .contact strong { font-weight: 700; }
  .contact__gap { height: 18px; }

  .cover-title {
    position: absolute; left: 0; top: 402px; width: 100%;
    text-align: center; font-style: italic; font-size: 27px; color: var(--brown);
  }
  .cover-band {
    position: absolute; left: 0; top: 447px; width: 100%; height: 249px;
    background: var(--white);
  }
</style>
</head>
<body>

  <section class="page page--back">
    <div class="top-strip"><span class="top-strip__title">Yoga Therapy and Meditation</span></div>

    <div class="brand-tab">
      <div class="brand-tab__dot"></div>
      <div class="brand-tab__name">VELINTU<br>AYURVEDIC</div>
    </div>

    <p class="intro">
      Only boutique Yoga Centre which practices Yoga in traditional way. Only six members in one session to provide personal attention to each member.Many different styles of Yoga, Meditation and Vinyasana.<br>
      Yoga and Ayurvedic Centre provides holistic approach in many ways with Ayurvedic doctors<br>
      and qualified therapists with an array of all naturopathic and Ayurvedic medicine.<br>
      Only Ayurvedic Centre with Therapeutic massage tables with made with Medicinal<br>
      wood and genuine herbal oils from India and Sri Lanka
    </p>

    <h2 class="schedule-title">VELINTU AYURVEDIC &amp; YOGA CENTRE</h2>
    <p class="schedule-sub">Spring 2013 <strong>INSTRUCTORS</strong> <strong>Arun Dessai</strong> &amp; <strong>Mirela Costa</strong></p>

    <table class="timetable">
      <colgroup>
        <col style="width:68px"><col style="width:60px"><col style="width:62px"><col style="width:62px">
        <col style="width:61px"><col style="width:61px"><col style="width:61px"><col style="width:62px">
      </colgroup>
      <tr><th>Period/Time</th><th>Monday</th><th>Tuesday</th><th>Wednesday</th><th>Thursday</th><th>Friday</th><th>Saturday</th><th>Sunday</th></tr>
      <tr><td class="rose">7.15 AM</td><td>Beginners</td><td class="rose">Power Yoga</td><td>Individual</td><td class="rose">Individual</td><td></td><td class="rose">Power Yoga</td><td></td></tr>
      <tr><td class="rose">9:00 AM</td><td></td><td class="rose"></td><td></td><td class="rose"></td><td></td><td class="rose">Beginners</td><td></td></tr>
      <tr><td class="rose">10:00 AM</td><td></td><td class="rose"></td><td></td><td class="rose"></td><td></td><td class="rose"></td><td></td></tr>
      <tr><td class="rose">12 Noon</td><td></td><td class="rose"></td><td></td><td class="rose"></td><td></td><td class="rose"></td><td></td></tr>
      <tr><td class="rose">6.30 PM</td><td></td><td class="rose">Beginners</td><td></td><td class="rose"></td><td></td><td class="rose"></td><td></td></tr>
      <tr><td class="rose">7.00 PM</td><td></td><td class="rose"></td><td>Pre-Natal</td><td class="rose">Pre-Natal</td><td></td><td class="rose"></td><td></td></tr>
      <tr><td class="rose">8.30 PM</td><td></td><td class="rose"></td><td></td><td class="rose"></td><td></td><td class="rose"></td><td></td></tr>
    </table>

    <div class="photo photo--sea" style="left:0;top:621px;width:170px;height:137px" role="img" aria-label="Woman kneeling on a yoga mat by the sea at dusk"></div>
    <div class="photo photo--stretch" style="left:170px;top:621px;width:180px;height:137px" role="img" aria-label="Woman stretching her arms overhead in a yoga pose"></div>

    <div class="contact">
      <strong>118 Linden Road,</strong><br>
      <strong>Westmere VIC 3190</strong><br>
      <strong>Email: hello@velintu.com.au</strong>
      <div class="contact__gap"></div>
      Please visit<br>
      <strong>www.velintu.com.au</strong><br>
      or call <strong>95550143</strong>
    </div>

    <div class="foot-strip">www.velintu.com.au</div>
  </section>

  <section class="page page--front">
    <div class="brand-tab">
      <div class="brand-tab__dot"></div>
      <div class="brand-tab__name">VELINTU<br>AYURVEDIC</div>
    </div>

    <h1 class="cover-title">Yoga Therapy and Meditation</h1>

    <div class="cover-band"></div>
    <div class="photo photo--sea-day" style="left:0;top:453px;width:287px;height:240px" role="img" aria-label="Woman kneeling on an orange yoga mat overlooking a coastal bay"></div>
    <div class="photo photo--stretch-day" style="left:287px;top:453px;width:273px;height:240px" role="img" aria-label="Woman stretching her clasped hands overhead"></div>

    <div class="foot-strip">www.velintu.com.au</div>
  </section>

</body>
</html>
```